Amazing wrap for KORVEL Summit LLC Brisk Haulmaxer 136" Wheelbase

Need a van wrap design. Full or Partial depends on designer idea. We are open for options. Currently we do not have a logo so that can be designed on the van as well.
include the following text, current email and phone are placeholders only.
Company Name. KORVEL SUMMIT LLC
website KORVELSUMMITPRO.COM
slogan: Elevate Your Comfort with Us
phone . 318-647-9051

Company is heating and cooling so we are open for the standard colors that are red white and blue or something very unique. .

Currently we dont have any design and would absolutely love to choose the best candidate from your submissions.

Prefer Partial wrap sides and back but open for full wrap options.

Open to an idea of mascot as well if you have something cool you are willing to make.

Attaching photos of the van that needs to be designed.

2023 Brisk Haulmaxer 136" Wheelbase. DO NOT SUBMIT OTHER SIZE VANS.

Open for something cool.

Target Market(s)

Mostly professional presentation to current customers.

Industry/Entity Type

Heating and Cooling Air conditioning etc.

Colors
0054AA
0677BA
7BADD7
CADEEF
E8F1F8
0094D4
00A9DD
6FCCEA
C7EBF8
E9F6FB
00AB8E
00BBA5
67D7C9
C6EFE9
E9F9F6
F0912C
F2A743
F7CA91
FBE8D2
FDF5EE
EE7325
F08F49
F5BC92
FAE3D3
FDF4ED
EB3D1F
EC4F4E
F09395
F8D3D4
FCEDEE

Requirements
Must have
• Name, Phone, Email. Awesome color combination. attention grabbing.
Nice to have
• No ideas, its open slate to submit your best option.

```html
<!DOCTYPE html>
<html lang="en">
<head>
<meta charset="utf-8">
<title>KORVEL Summit LLC – Van Wrap</title>
<link rel="stylesheet" href="https://fonts.googleapis.com/css2?family=Montserrat:wght@800&family=Barlow+Semi+Condensed:wght@500&family=Barlow+Condensed:ital,wght@0,700;1,700&family=Russo+One&display=swap">
<style>
  :root {
    --blue: #1a6fb3;
    --blue-light: #2a8ed0;
    --blue-deep: #0d4c8a;
    --red: #b9252f;
    --red-deep: #7c1820;
    --red-text: #9e1f28;
    --white: #ffffff;
    --page: #ffffff;
  }
  html, body {
    margin: 0;
    width: 1200px;
    height: 3300px;
    overflow: hidden;
    background: var(--page);
  }
  .wrap-sheet {
    position: relative;
    width: 1200px;
    height: 3300px;
  }
  .side-panel {
    position: absolute;
    left: 50px;
    top: 760px;
    width: 1100px;
    height: 548px;
  }
  .rear-panel {
    position: absolute;
    left: 200px;
    top: 1660px;
    width: 800px;
    height: 800px;
  }
  .brand-name { font-family: "Montserrat", sans-serif; font-weight: 800; fill: var(--white); }
  .brand-sub { font-family: "Barlow Semi Condensed", sans-serif; font-weight: 500; fill: var(--white); }
  .phone-red { font-family: "Russo One", sans-serif; fill: var(--red-text); }
  .phone-white { font-family: "Barlow Condensed", sans-serif; font-weight: 700; fill: var(--white); }
  .slogan { font-family: "Russo One", sans-serif; fill: var(--white); }
  .web-red { font-family: "Barlow Condensed", sans-serif; font-weight: 700; font-style: italic; fill: var(--red-text); }
  .web-white { font-family: "Barlow Condensed", sans-serif; font-weight: 700; fill: var(--white); }
</style>
</head>
<body>
<main class="wrap-sheet">

  <!-- Driver side layout -->
  <svg class="side-panel" viewBox="0 0 682 340" xmlns="http://www.w3.org/2000/svg">
    <defs>
      <linearGradient id="blueFill" x1="0" y1="0" x2="1" y2="1">
        <stop offset="0" stop-color="#2a8ed0"/>
        <stop offset="1" stop-color="#0d4c8a"/>
      </linearGradient>
      <linearGradient id="redFill" x1="0" y1="0" x2="1" y2="0">
        <stop offset="0" stop-color="#7c1820"/>
        <stop offset="1" stop-color="#c02a33"/>
      </linearGradient>
      <linearGradient id="mascotFill" x1="0" y1="0" x2="0" y2="1">
        <stop offset="0" stop-color="#f1f1f1"/>
        <stop offset="1" stop-color="#2b6fb2"/>
      </linearGradient>
    </defs>
    <rect class="panel-base" width="682" height="340" fill="var(--white)"/>
    <!-- blue body -->
    <path class="blue-body" d="M500 0 H682 V340 H0 V270 C30 240 50 210 80 195 C200 170 300 150 360 120 C420 90 460 40 500 0 Z" fill="url(#blueFill)"/>
    <!-- red accent stripe -->
    <path class="red-accent" d="M470 0 H530 C480 50 430 100 370 125 L350 130 C410 95 440 45 470 0 Z" fill="var(--red)"/>
    <!-- slogan band -->
    <path class="slogan-band" d="M682 135 V225 C580 240 470 260 380 300 L360 275 C430 205 560 160 682 135 Z" fill="url(#redFill)"/>
    <path class="band-edge" d="M380 300 C470 260 580 240 682 225" stroke="var(--white)" stroke-width="4" fill="none"/>
    <!-- lower diagonal stripes -->
    <path class="low-stripe-white" d="M190 340 L240 340 L420 285 L400 282 Z" fill="var(--white)"/>
    <path class="low-stripe-red" d="M240 340 L300 340 C420 300 520 280 682 262 V250 C540 262 420 285 240 340 Z" fill="var(--red)"/>
    <!-- website pill -->
    <path class="web-pill" d="M60 210 C120 200 200 195 240 192 L236 222 C180 225 110 228 55 232 Z" fill="var(--white)"/>
    <text class="web-red" x="72" y="223" font-size="19" transform="rotate(-2 72 223)">KorvelSummitPro.com</text>
    <!-- phone -->
    <text class="phone-red" x="232" y="66" font-size="21" transform="rotate(-3 232 66)">318-647-9051</text>
    <!-- mascot -->
    <rect x="262" y="70" width="110" height="200" rx="24" fill="url(#mascotFill)" role="img" aria-label="Cartoon HVAC technician mascot holding manifold gauges, giving a thumbs up"/>
    <!-- brand -->
    <text class="brand-name" x="440" y="130" font-size="52" transform="rotate(-17 440 130)">KORVEL</text>
    <text class="brand-sub" x="432" y="172" font-size="34" transform="rotate(-17 432 172)">Summit LLC</text>
    <!-- slogan -->
    <text class="slogan" x="440" y="240" font-size="17" transform="rotate(-12 440 240)">ELEVATE YOUR</text>
    <text class="slogan" x="430" y="265" font-size="17" transform="rotate(-12 430 265)">COMFORT WITH US</text>
  </svg>

  <!-- Rear doors layout -->
  <svg class="rear-panel" viewBox="0 0 400 400" xmlns="http://www.w3.org/2000/svg">
    <defs>
      <linearGradient id="rearBlue" x1="0" y1="0" x2="0" y2="1">
        <stop offset="0" stop-color="#0f5796"/>
        <stop offset="1" stop-color="#2a86c6"/>
      </linearGradient>
      <linearGradient id="rearRed" x1="0" y1="0" x2="1" y2="0">
        <stop offset="0" stop-color="#9d1f28"/>
        <stop offset="1" stop-color="#c02a33"/>
      </linearGradient>
      <linearGradient id="rearMascot" x1="0" y1="0" x2="0" y2="1">
        <stop offset="0" stop-color="#f1f1f1"/>
        <stop offset="1" stop-color="#2b6fb2"/>
      </linearGradient>
    </defs>
    <rect class="rear-base" width="400" height="400" fill="url(#rearBlue)"/>
    <path class="rear-red-band" d="M0 172 C130 160 270 160 400 175 V270 C270 255 130 262 0 290 Z" fill="url(#rearRed)"/>
    <path d="M0 172 C130 160 270 160 400 175" stroke="var(--white)" stroke-width="3" fill="none"/>
    <path d="M0 290 C130 262 270 255 400 270" stroke="var(--white)" stroke-width="4" fill="none"/>
    <rect x="205" y="48" width="150" height="220" rx="28" fill="url(#rearMascot)" role="img" aria-label="Cartoon HVAC technician mascot holding manifold gauges, giving a thumbs up"/>
    <text class="brand-name" x="128" y="100" font-size="32" text-anchor="middle">KORVEL</text>
    <text class="brand-sub" x="128" y="128" font-size="24" text-anchor="middle">Summit LLC</text>
    <text class="phone-white" x="128" y="198" font-size="24" text-anchor="middle">318-647-9051</text>
    <text class="web-white" x="128" y="218" font-size="15" text-anchor="middle">KorvelSummitPro.com</text>
    <text class="slogan" x="268" y="296" font-size="15" text-anchor="middle">ELEVATE YOUR</text>
    <text class="slogan" x="268" y="316" font-size="15" text-anchor="middle">COMFORT</text>
    <text class="slogan" x="268" y="336" font-size="15" text-anchor="middle">WITH US</text>
  </svg>

</main>
</body>
</html>
```